Business Card Design

Cedar Gate Rentals
Cedar Gate Rentals is a high end home rental leasing company that provides exquisite properties in niche markets. We are a small family owned business that considers our clients not as renters, but as friends. Every property we buy must be brought up to our high standards before it is offered on the market. The properties that we lease are exceptional, "move in" ready homes. This allows for the client to take pride in their lease as if it was their own home. To put it another way; we do not lease a property that we would not live in ourselves.

Target Market(s)

Couples making $100K or more

Industry/Entity Type

Business

Requirements
Must have
• Some sort of logo
Nice to have
• good slogan
Should not have
• Pink

```html
<!DOCTYPE html>
<html lang="en">
<head>
<meta charset="utf-8">
<title>Cedar Gate Rentals – Business Card</title>
<link rel="stylesheet" href="https://fonts.googleapis.com/css2?family=Arimo:wght@400;700&family=Michroma&display=swap">
<style>
  :root {
    --backdrop: #6a6766;
    --card: #1b1b1c;
    --wedge: #4a4a4b;
    --band: #333334;
    --brand: #8c88c4;
    --name: #c4f1f1;
    --title: #9fb7c2;
    --contact: #7cc3c2;
  }
  html, body {
    margin: 0;
    width: 1200px;
    height: 1000px;
    overflow: hidden;
    background: var(--backdrop);
  }
  .card {
    position: absolute;
    left: 120px;
    top: 226px;
    width: 960px;
    height: 548px;
    background: var(--card);
    overflow: hidden;
    box-shadow: 0 18px 40px rgba(0,0,0,.45);
  }
  .card-wedge {
    position: absolute;
    left: 0;
    top: 0;
  }
  .brand {
    position: absolute;
    right: 70px;
    top: 120px;
    display: flex;
    align-items: center;
    gap: 16px;
    font-family: "Arimo", sans-serif;
    font-weight: 700;
    font-size: 44px;
    color: var(--brand);
  }
  .brand-square {
    width: 34px;
    height: 34px;
    background: var(--brand);
  }
  .name-band {
    position: absolute;
    left: 420px;
    right: 0;
    top: 222px;
    height: 112px;
    background: var(--band);
  }
  .person-name {
    position: absolute;
    right: 36px;
    top: 58px;
    margin: 0;
    font-family: "Michroma", sans-serif;
    font-size: 27px;
    font-weight: 400;
    letter-spacing: 2px;
    color: var(--name);
  }
  .person-title {
    position: absolute;
    left: 54px;
    top: 16px;
    margin: 0;
    font-family: "Arimo", sans-serif;
    font-size: 20px;
    letter-spacing: 6px;
    color: var(--title);
  }
  .contact-list {
    position: absolute;
    left: 432px;
    top: 366px;
    margin: 0;
    padding: 0;
    list-style: none;
    font-family: "Arimo", sans-serif;
    font-size: 22px;
    color: var(--contact);
  }
  .contact-list li {
    display: flex;
    align-items: center;
    gap: 14px;
    height: 34px;
  }
  .contact-icon {
    width: 22px;
    height: 22px;
    fill: var(--contact);
  }
</style>
</head>
<body>
  <div class="card">
    <svg class="card-wedge" width="960" height="548" viewBox="0 0 960 548" aria-hidden="true">
      <polygon points="0,0 0,548 190,548" fill="var(--wedge)"/>
    </svg>

    <div class="brand">
      <span class="brand-square"></span>
      <span class="brand-name">Cedar Gate Rentals</span>
    </div>

    <div class="name-band">
      <p class="person-title">entrepreneur</p>
      <h1 class="person-name">MARCUS DELANO</h1>
    </div>

    <ul class="contact-list">
      <li>
        <svg class="contact-icon" viewBox="0 0 24 24" aria-hidden="true"><path d="M6.6 10.8a15.1 15.1 0 0 0 6.6 6.6l2.2-2.2a1 1 0 0 1 1-.25 11.4 11.4 0 0 0 3.6.57 1 1 0 0 1 1 1V20a1 1 0 0 1-1 1A17 17 0 0 1 3 4a1 1 0 0 1 1-1h3.5a1 1 0 0 1 1 1c0 1.25.2 2.45.57 3.57a1 1 0 0 1-.25 1z"/></svg>
        <span>555-014-2290</span>
      </li>
      <li>
        <svg class="contact-icon" viewBox="0 0 24 24" aria-hidden="true"><path d="M2 5h20v14H2z M2 5l10 8 10-8" fill="var(--contact)" stroke="var(--card)" stroke-width="1.5"/></svg>
        <span>cedargaterentals@mailbrook.com</span>
      </li>
      <li>
        <svg class="contact-icon" viewBox="0 0 24 24" aria-hidden="true"><path d="M12 2a7 7 0 0 0-7 7c0 5 7 13 7 13s7-8 7-13a7 7 0 0 0-7-7zm0 9.5A2.5 2.5 0 1 1 12 6.5a2.5 2.5 0 0 1 0 5z"/></svg>
        <span>Linden Circle Westbrook, OH 44000</span>
      </li>
    </ul>
  </div>
</body>
</html>
```